Design WORDPRESS Website for E Commerce Business

We are needing a WORDPRESS website for an E Commerce Business that is supplying quailty kids / baby products.

Target Market(s)

Female / Working Mums / New Mums

Industry/Entity Type

Business

Number of Pages Required

1 page

Font styles to use
Sans Serif

Colors
33b8a4
f8fcfd
d3a5cc
f7f1f7
cbcbcb
9d9d9d

```html
<!DOCTYPE html>
<html lang="en">
<head>
<meta charset="utf-8">
<title>Tot &amp; Tumble – Quality Baby &amp; Kids Products</title>
<link href="https://fonts.googleapis.com/css2?family=Nunito:wght@300;400;600;700;800&display=swap" rel="stylesheet">
<style>
:root{
  --sky:#a9dcf2;
  --sky-deep:#6ec3e6;
  --sky-pale:#e6f5fb;
  --peach:#f6c1ae;
  --peach-pale:#fbe3da;
  --pink-pale:#fbe1e0;
  --teal-dark:#3b8ea6;
  --ink:#1d1d1d;
  --grey:#9d9d9d;
  --grey-light:#cbcbcb;
  --band:#f5f6f7;
  --white:#ffffff;
}
*{box-sizing:border-box;margin:0;padding:0}
html,body{width:1200px;height:4306px;overflow:hidden}
body{position:relative;background:var(--white);font-family:'Nunito',sans-serif;color:var(--ink)}
.abs{position:absolute}
.ph{display:block}

/* header */
.hero-media{left:0;top:0;width:1200px;height:680px;background:linear-gradient(120deg,#9fc4cc 0%,#c9dde0 35%,#e8d7cf 60%,#d9c2b6 80%,#b9cfd6 100%)}
.hero-wave{left:0;top:590px;width:1200px;height:110px}
.logo-disc{left:130px;top:-95px;width:200px;height:200px;border-radius:50%;background:var(--white);display:flex;align-items:flex-end;justify-content:center;padding-bottom:44px}
.brand{font-family:'Nunito',sans-serif;font-weight:700;color:var(--sky-deep);font-size:24px;line-height:1;display:flex;align-items:center;gap:8px}
.brand .dot{width:14px;height:14px;border-radius:50%;background:var(--sky-deep)}
.search{left:402px;top:30px;width:236px;height:28px;border:1.5px solid rgba(255,255,255,.85);border-radius:14px;color:#fff;font-size:12px;padding:5px 14px}
.search svg{position:absolute;right:12px;top:7px}
.nav-link{top:34px;color:#fff;font-size:13px;font-weight:600;display:flex;align-items:center;gap:5px}
.menu-pill{left:968px;top:28px;width:82px;height:30px;border-radius:15px;background:var(--sky);color:#fff;font-size:13px;font-weight:700;display:flex;align-items:center;justify-content:center;gap:6px}
.hero-title{left:138px;top:280px;width:460px;color:#fff;font-weight:300;font-size:40px;line-height:50px}
.btn{display:flex;align-items:center;justify-content:center;background:var(--peach);color:#fff;font-weight:700;text-transform:uppercase;letter-spacing:.5px;border-radius:25px}
.hero-btn{left:132px;top:452px;width:228px;height:52px;font-size:14px;font-weight:600}
.chev{width:44px;height:44px;border-radius:50%;background:var(--sky);display:flex;align-items:center;justify-content:center}
.chev-hero{left:580px;top:625px;background:transparent;border:2px solid #fff}

/* sections */
.sec-title{left:0;width:1200px;text-align:center;font-size:25px;font-weight:600;letter-spacing:1px}
.collection{width:252px;height:252px;border-radius:50%;border:9px solid var(--sky);overflow:hidden;background:#fff}
.collection .ph{width:100%;height:100%}
.collection .label{position:absolute;left:0;bottom:0;width:100%;height:72px;display:flex;align-items:flex-start;justify-content:center;padding-top:14px;color:#fff;font-size:30px;font-weight:600}

.card{width:290px;text-align:center}
.card .media{position:relative;height:193px;background:#f1f1f1}
.card .media .ph{width:100%;height:100%}
.tag{position:absolute;left:0;top:0;height:24px;padding:0 24px 0 10px;background:var(--sky);color:#fff;font-size:11px;line-height:24px;clip-path:polygon(0 0,100% 0,78% 100%,0 100%)}
.card .name{margin-top:38px;color:var(--sky-deep);font-size:20px;font-weight:600}
.card .sub{margin-top:6px;color:var(--grey);font-size:10px}
.card .price{margin-top:14px;font-size:25px;font-weight:700}
.card .btn{margin:20px auto 0;width:187px;height:38px;font-size:13px}
.card.raised .media{background:#fff;box-shadow:0 4px 20px rgba(0,0,0,.14)}

.grey-band{left:0;top:1850px;width:1200px;height:780px}
.arrow{top:2310px}

.tile{background:#f6f6f6;border:1px solid #ececec}
.tile .ph{width:100%;height:100%}
.tile-text{text-align:center;background:#f6f6f6}
.tile-text .name{margin-top:34px;color:var(--sky-deep);font-size:20px;font-weight:600}
.tile-text .sub{margin-top:6px;color:var(--grey);font-size:10px}
.tile-text .price{margin-top:14px;font-size:25px;font-weight:700}
.tile-text .btn{margin:18px auto 0;width:144px;height:32px;font-size:12px}
.girl-caption{color:#fff;text-align:center;font-size:17px;font-weight:600}
.girl-caption small{display:block;font-size:10px;font-weight:400;margin-top:4px}

.promo{left:0;top:3330px;width:1200px;height:505px;background:linear-gradient(180deg,#f3f4f5,#fafafa)}
.promo-art{left:86px;top:3385px;width:450px;height:380px;border-radius:40px;background:radial-gradient(ellipse at 50% 55%,#e9a36a 0%,#d8795a 35%,#8ec9e3 65%,rgba(243,244,245,0) 80%)}
.promo-copy{left:570px;top:3480px;width:400px;text-align:center}
.promo-copy .kicker{color:var(--sky-deep);font-size:22px}
.promo-copy .big{color:var(--sky);font-size:96px;font-weight:800;line-height:92px;letter-spacing:2px}
.promo-copy .off{color:var(--peach);font-size:54px;font-weight:700;line-height:58px}
.promo-copy p{margin-top:16px;color:var(--grey);font-size:11px;line-height:16px}
.promo-copy .btn{margin:26px auto 0;width:168px;height:38px;font-size:12px}

/* footer */
.footer-disc{left:503px;top:3775px;width:200px;height:200px;border-radius:50%;background:#fff;border:2px solid var(--peach-pale);display:flex;align-items:center;justify-content:center}
.f-head{top:3990px;font-size:15px;font-weight:600}
.f-list{top:4038px;list-style:none;font-size:12px;color:#555;line-height:27px}
.news-input{left:150px;top:4050px;width:375px;height:34px;border-radius:17px;background:#f6f6f6;font-size:11px;color:var(--grey);padding:9px 18px}
.news-input .btn{position:absolute;right:0;top:0;width:120px;height:34px;font-size:12px;border-radius:17px}
.social{left:152px;top:4172px;display:flex;gap:12px}
.social span{width:12px;height:12px;border-radius:50%;background:var(--grey-light)}
.f-rule{left:0;top:4240px;width:1200px;height:1px;background:#e6e6e6}
.copyright{left:0;top:4266px;width:1200px;text-align:center;font-size:12px;font-weight:600}
</style>
</head>
<body>

<!-- HERO -->
<div class="abs hero-media ph" role="img" aria-label="Photo of a mother and her young daughter sharing a tender moment at home"></div>
<svg class="abs hero-wave" viewBox="0 0 1200 110" preserveAspectRatio="none">
  <path d="M0 40 Q60 0 120 30 Q200 80 280 45 Q360 10 440 45 Q520 80 600 50 Q680 15 760 45 Q840 80 920 45 Q1000 10 1080 40 Q1140 62 1200 30 L1200 110 L0 110Z" fill="#cfeaf6"/>
  <path d="M0 60 Q60 22 120 50 Q200 96 280 64 Q360 30 440 64 Q520 98 600 70 Q680 36 760 64 Q840 98 920 64 Q1000 30 1080 58 Q1140 80 1200 52 L1200 110 L0 110Z" fill="#fff"/>
</svg>

<header>
  <div class="abs logo-disc"><span class="brand"><span class="dot"></span>Tot &amp; Tumble</span></div>
  <div class="abs search">Search
    <svg width="12" height="12" viewBox="0 0 12 12"><circle cx="5" cy="5" r="3.8" fill="none" stroke="#fff" stroke-width="1.5"/><line x1="8" y1="8" x2="11" y2="11" stroke="#fff" stroke-width="1.5"/></svg>
  </div>
  <div class="abs nav-link" style="left:798px">Wishlist
    <svg width="13" height="12" viewBox="0 0 13 12"><path d="M6.5 11 L1.5 6 A2.8 2.8 0 0 1 6.5 2 A2.8 2.8 0 0 1 11.5 6Z" fill="#fff"/></svg></div>
  <div class="abs nav-link" style="left:893px">Cart
    <svg width="14" height="12" viewBox="0 0 14 12"><path d="M0 1 H3 L5 8 H12 L13 3 H4" fill="none" stroke="#fff" stroke-width="1.5"/><circle cx="6" cy="10.5" r="1.2" fill="#fff"/><circle cx="11" cy="10.5" r="1.2" fill="#fff"/></svg></div>
  <div class="abs menu-pill">Menu
    <svg width="12" height="10" viewBox="0 0 12 10"><path d="M0 1H12M0 5H12M0 9H12" stroke="#fff" stroke-width="1.6"/></svg></div>
</header>

<h1 class="abs hero-title">Tot &amp; Tumble will be supplying quality baby / kids products</h1>
<div class="abs btn hero-btn">View Collections</div>
<div class="abs chev chev-hero"><svg width="16" height="10" viewBox="0 0 16 10"><path d="M2 2 L8 8 L14 2" fill="none" stroke="#fff" stroke-width="2"/></svg></div>

<!-- COLLECTIONS -->
<h2 class="abs sec-title" style="top:795px">OUR COLLECTIONS</h2>
<div class="abs collection" style="left:161px;top:893px">
  <div class="ph" role="img" aria-label="Photo of a smiling young boy" style="background:linear-gradient(160deg,#e9e3dc,#c9a98e)"></div>
  <div class="label" style="background:var(--sky)">Boys</div>
</div>
<div class="abs collection" style="left:471px;top:893px;border-color:#f3f3f3">
  <div class="ph" role="img" aria-label="Photo of a little girl playing" style="background:linear-gradient(160deg,#f1ece6,#e2c5b4)"></div>
  <div class="label" style="background:var(--peach)">Girls</div>
</div>
<div class="abs collection" style="left:781px;top:893px;border-color:#f3f3f3">
  <div class="ph" role="img" aria-label="Photo of a mother with her child" style="background:linear-gradient(160deg,#f3eeea,#d7b9a6)"></div>
  <div class="label" style="background:var(--teal-dark)">Moms</div>
</div>

<!-- BOYS -->
<h2 class="abs sec-title" style="top:1268px">BOYS</h2>
<article class="abs card" style="left:144px;top:1360px">
  <div class="media"><div class="ph" role="img" aria-label="Photo of colourful toy vehicles" style="background:linear-gradient(135deg,#7ab6d9,#d9c7a6 60%,#e66c5e)"></div><span class="tag">Toys</span></div>
  <div class="name">Tot &amp; Tumble 1</div><div class="sub">Soft toys with jacket</div><div class="price">$62.00</div><div class="btn">Add to cart</div>
</article>
<article class="abs card" style="left:455px;top:1360px">
  <div class="media"><div class="ph" role="img" aria-label="Photo of denim jeans and blue baby shoes" style="background:linear-gradient(135deg,#c9ccd0,#4b6aa3 55%,#2d4b80)"></div><span class="tag">Clothes</span></div>
  <div class="name">Tot &amp; Tumble 2</div><div class="sub">Soft toys with jacket</div><div class="price">$12.00</div><div class="btn">Add to cart</div>
</article>
<article class="abs card" style="left:766px;top:1360px">
  <div class="media"><div class="ph" role="img" aria-label="Photo of a red and yellow toy truck" style="background:radial-gradient(circle at 50% 55%,#e8c23a 0%,#d64b3b 30%,#f6f6f6 55%)"></div><span class="tag">Toys</span></div>
  <div class="name">Tot &amp; Tumble 3</div><div class="sub">Soft toys with jacket</div><div class="price">$22.00</div><div class="btn">Add to cart</div>
</article>
<div class="abs chev" style="left:590px;top:1780px;width:36px;height:36px"><svg width="14" height="9" viewBox="0 0 14 9"><path d="M2 2 L7 7 L12 2" fill="none" stroke="#fff" stroke-width="2"/></svg></div>

<!-- FEATURED -->
<svg class="abs grey-band" viewBox="0 0 1200 780" preserveAspectRatio="none">
  <path d="M0 40 Q300 -10 600 30 Q900 70 1200 20 L1200 740 Q900 790 600 750 Q300 710 0 760Z" fill="var(--band)"/>
</svg>
<h2 class="abs sec-title" style="top:1997px">FEATURED PRODUCTS</h2>
<article class="abs card raised" style="left:144px;top:2109px">
  <div class="media"><div class="ph" role="img" aria-label="Photo of a plush dragon toy" style="background:radial-gradient(circle at 50% 50%,#4fc2c4 0%,#9ad9d6 25%,#fff 50%)"></div><span class="tag">Toys</span></div>
  <div class="name">Tot &amp; Tumble 4</div><div class="sub">Soft toys with jacket</div><div class="price">$52.00</div><div class="btn">Add to cart</div>
</article>
<article class="abs card raised" style="left:455px;top:2109px">
  <div class="media"><div class="ph" role="img" aria-label="Photo of a navy striped girls dress" style="background:radial-gradient(ellipse at 50% 50%,#2a3552 0%,#55607c 28%,#fff 52%)"></div><span class="tag">Clothes</span></div>
  <div class="name">Tot &amp; Tumble 5</div><div class="sub">Soft toys with jacket</div><div class="price">$132.00</div><div class="btn">Add to cart</div>
</article>
<article class="abs card raised" style="left:766px;top:2109px">
  <div class="media"><div class="ph" role="img" aria-label="Photo of a plush giraffe toy" style="background:radial-gradient(circle at 50% 50%,#f0b93a 0%,#f6d88a 25%,#fff 50%)"></div><span class="tag">Toys</span></div>
  <div class="name">Tot &amp; Tumble 6</div><div class="sub">Soft toys with jacket</div><div class="price">$142.00</div><div class="btn">Add to cart</div>
</article>
<svg class="abs arrow" style="left:60px" width="14" height="24" viewBox="0 0 14 24"><path d="M11 2 L3 12 L11 22" fill="none" stroke="#9d9d9d" stroke-width="2"/></svg>
<svg class="abs arrow" style="left:1126px" width="14" height="24" viewBox="0 0 14 24"><path d="M3 2 L11 12 L3 22" fill="none" stroke="#9d9d9d" stroke-width="2"/></svg>

<!-- NEW ARRIVALS -->
<h2 class="abs sec-title" style="top:2692px">NEW ARRIVALS</h2>
<div class="abs tile" style="left:144px;top:2784px;width:290px;height:193px;background:var(--pink-pale)">
  <div class="ph" role="img" aria-label="Photo of a purple girls dress" style="background:radial-gradient(ellipse at 50% 50%,#6a2c6f 0%,#9a5a9c 30%,var(--pink-pale) 55%)"></div>
  <div class="abs girl-caption" style="left:0;top:82px;width:290px">Girl Clothes<small>Shop now for girls</small></div>
</div>
<div class="abs tile" style="left:455px;top:2784px;width:290px;height:193px;background:#fff">
  <div class="ph" role="img" aria-label="Photo of a stack of colourful kids t-shirts" style="background:radial-gradient(ellipse at 50% 50%,#d8402f 0%,#3c7fc4 25%,#f3f3f3 50%,#fff 60%)"></div>
</div>
<div class="abs tile" style="left:766px;top:2784px;width:290px;height:193px;background:#fff">
  <div class="ph" role="img" aria-label="Photo of a green kids hooded jacket" style="background:radial-gradient(ellipse at 50% 50%,#4d8c80 0%,#8abdb3 28%,#fff 52%)"></div>
</div>
<div class="abs tile" style="left:144px;top:2999px;width:290px;height:200px;background:#fff">
  <div class="ph" role="img" aria-label="Photo of a plush puppy toy" style="background:radial-gradient(ellipse at 50% 50%,#a46a3a 0%,#cc9a6a 28%,#fff 52%)"></div>
</div>
<div class="abs tile tile-text" style="left:455px;top:2999px;width:290px;height:200px">
  <div class="name">Tot &amp; Tumble 7</div><div class="sub">Soft toys with jacket</div><div class="price">$112.00</div><div class="btn">View Details</div>
</div>
<div class="abs tile" style="left:766px;top:2999px;width:290px;height:200px;background:#fff">
  <div class="ph" role="img" aria-label="Photo of stacking rings and a plush bear" style="background:radial-gradient(ellipse at 50% 50%,#e2433a 0%,#f0c23b 22%,#4aa8d8 34%,#fff 55%)"></div>
</div>
<div class="abs chev" style="left:590px;top:3255px;width:36px;height:36px"><svg width="14" height="9" viewBox="0 0 14 9"><path d="M2 2 L7 7 L12 2" fill="none" stroke="#fff" stroke-width="2"/></svg></div>

<!-- PROMO -->
<div class="abs promo"></div>
<div class="abs promo-art ph" role="img" aria-label="Illustration of a teddy bear, toy truck, stacking rings and toy train"></div>
<div class="abs promo-copy">
  <div class="kicker">Tot &amp; Tumbles</div>
  <div class="big">TOYS</div>
  <div class="off">15% OFFER</div>
  <p>Soft plush toys, bright stacking sets and sturdy trucks made for little hands to explore and enjoy.</p>
  <div class="btn">Shop Now</div>
</div>

<!-- FOOTER -->
<footer>
  <div class="abs footer-disc"><span class="brand"><span class="dot"></span>Tot &amp; Tumble</span></div>

  <div class="abs f-head" style="left:152px">Sign Up For Newsletter</div>
  <div class="abs news-input">Enter Your E-Newsletter<div class="btn">Subscribe</div></div>
  <div class="abs f-head" style="left:148px;top:4128px">Connect With Us</div>
  <div class="abs social"><span></span><span></span><span></span><span></span><span></span></div>

  <div class="abs f-head" style="left:562px">Quick Links</div>
  <ul class="abs f-list" style="left:562px"><li>Home</li><li>About Us</li><li>Products</li><li>Stores</li><li>Locations</li><li>Contact Us</li></ul>

  <div class="abs f-head" style="left:745px">Other Links</div>
  <ul class="abs f-list" style="left:745px"><li>Privacy Policy</li><li>Terms Of Use</li><li>Help</li><li>Disclaimer</li></ul>

  <div class="abs f-head" style="left:900px">Support Links</div>
  <ul class="abs f-list" style="left:900px"><li>My Order</li><li>Track Order</li><li>Affiliate Program</li><li>Returns</li><li>24x7 Customer Support</li></ul>

  <div class="abs f-rule"></div>
  <div class="abs copyright">© 2017 Company Name &nbsp;| All Rights Reserved</div>
</footer>

</body>
</html>
```